Harbor Quill is a Smart Device and Wiring Business offering the latest in Smart Home Devices inc

Looking for a new website to draw people to my business and explain what a smart home is all about. I currently own a domain and have a website I put together in webnimbus business website builder. address www.harborquill.com. The website needs modernising and be visually appealing with cool action buttons, client feedback page etc.

The webpage needs to present an image of seamless integration of wireless voice control and smart devices that take tasks and activities away from the owner saving them time and money.

I have a chatterbay business page(harbor quill) and snapmeadow linked with the business, are we able to link this to the website somehow?

Target Market(s)

Residential home owners who want to modernise their home. Who have seen adverts for orbit nook and kestrel nova and want to put it in their home.

Industry/Entity Type

Technology Equipment

Number of Pages Required

1 page

Colors

Designer to choose colors to be used in the design.

Requirements
Must have
• A great landing page, that is modern and attractive, that gets across the idea of smart devices and technology.
• Must be ios/android device friendly.
Nice to have
• interactive/animated buttons
• I like the direction and interactiveness of these websites, a simplified version would be awesome.
• Something in between:
• http://www.oakridgelofts.com/ and https://plumcove.com/
• http://www.oakridgelofts.com/

```html
<!DOCTYPE html>
<html lang="en">
<head>
<meta charset="utf-8">
<title>Harbor Quill — Smart Homes</title>
<link href="https://fonts.googleapis.com/css2?family=Arimo:wght@400;500;600;700&display=swap" rel="stylesheet">
<style>
  :root{
    --ink:#111;
    --white:#fff;
    --violet:#b36ef0;
    --violet-deep:#7d6fe6;
    --periwinkle:#5b76d8;
    --sky:#4ab8e8;
    --teal:#52c7d8;
    --blue:#4a9fe0;
    --night:#202020;
    --hero-dark:#1c2230;
    --footer:#6a9fe6;
    --yellow:#f5d10a;
  }
  *{box-sizing:border-box;margin:0;padding:0}
  html,body{width:1200px;height:2951px;overflow:hidden}
  body{font-family:"Arimo",Helvetica,Arial,sans-serif;color:var(--ink);background:var(--white);position:relative}
  .abs{position:absolute}

  /* header */
  .site-header{position:absolute;left:0;top:0;width:1200px;height:76px;background:var(--white);border-bottom:4px solid #26333f}
  .brand{position:absolute;left:140px;top:18px;display:flex;align-items:center;gap:10px}
  .brand-dot{width:40px;height:40px;border-radius:50%;background:var(--blue)}
  .brand-name{font-size:22px;font-weight:700;color:#1b2a3a;letter-spacing:1px}
  .main-nav{position:absolute;top:28px;left:675px;display:flex;gap:32px;font-size:17px;color:#333}
  .main-nav .current{color:var(--blue);border-bottom:2px solid var(--blue);padding-bottom:4px}

  /* hero */
  .hero{position:absolute;left:0;top:76px;width:1200px;height:472px;background:linear-gradient(100deg,#2a2d38 0%,#1b2030 45%,#3a3a48 100%)}
  .hero-device{position:absolute;left:755px;top:86px;width:316px;height:316px;border-radius:50%;background:radial-gradient(circle at 40% 35%,#f4f4f4,#c9c9c9)}
  .hero-title{position:absolute;left:138px;top:130px;font-size:82px;font-weight:700;line-height:76px;letter-spacing:1px;background:linear-gradient(90deg,#b36ef0,#8c8cf0);-webkit-background-clip:text;background-clip:text;color:transparent}
  .hero-tagline{position:absolute;left:142px;top:286px;font-size:26px;color:var(--white)}
  .btn{display:inline-block;border-radius:24px;color:var(--white);text-align:center}
  .hero-btn{position:absolute;left:140px;top:336px;width:166px;height:46px;line-height:46px;font-size:18px;background:linear-gradient(90deg,var(--violet),var(--violet-deep))}

  /* about */
  .about{position:absolute;left:0;top:548px;width:1200px;height:442px;background:linear-gradient(115deg,var(--violet) 0%,#8a72e6 55%,var(--periwinkle) 100%);color:var(--white)}
  .about-label{position:absolute;left:142px;top:82px;font-size:21px;font-weight:700;padding-bottom:6px;border-bottom:2px solid var(--white)}
  .about-title{position:absolute;left:142px;top:132px;font-size:26px;font-weight:700}
  .about-text{position:absolute;left:142px;top:178px;width:590px;font-size:19px;line-height:30px}
  .about-art{position:absolute;left:785px;top:85px;width:275px;height:245px;border-radius:8px;background:linear-gradient(135deg,rgba(255,255,255,.18),rgba(255,255,255,.04))}
  .slider-dots{position:absolute;left:570px;top:380px;display:flex;gap:22px}
  .slider-dots span{width:20px;height:20px;border-radius:50%;border:2px solid var(--sky)}
  .slider-dots span.on{border:none;background:#d8c8f8;width:16px;height:16px;margin-top:2px}

  /* services */
  .services{position:absolute;left:0;top:990px;width:1200px;height:643px}
  .service-icon{position:absolute;left:140px;top:128px;width:136px;height:114px;border:4px solid var(--blue);background:linear-gradient(135deg,rgba(82,199,216,.35),rgba(74,159,224,.35))}
  .service-title{position:absolute;left:140px;top:250px;font-size:26px;font-weight:700;color:var(--blue)}
  .service-text{position:absolute;left:140px;top:290px;width:320px;font-size:17px;line-height:30px}
  .service-photo{position:absolute;left:467px;top:73px;width:573px;height:295px;background:linear-gradient(120deg,#1a1e2a,#3b3f52 50%,#1c1d26)}
  .service-steps{position:absolute;left:0;top:0;width:1200px;height:643px}
  .step-label{position:absolute;width:150px;text-align:center;font-size:22px;line-height:28px;color:var(--teal)}

  /* package */
  .package{position:absolute;left:0;top:1633px;width:1200px;height:492px;background:var(--night);color:var(--white)}
  .package-ring{position:absolute;left:142px;top:174px;width:216px;height:216px;border-radius:50%;border:3px solid var(--sky);display:flex;align-items:center;justify-content:center;text-align:center;font-size:30px;line-height:36px;color:var(--sky)}
  .package-toggle{position:absolute;top:425px;width:55px;height:16px;border-radius:8px}
  .package-cost{position:absolute;left:430px;top:185px;font-size:23px;color:var(--sky)}
  .package-cost b{font-weight:700}
  .package-text{position:absolute;left:430px;top:220px;width:290px;font-size:17px;line-height:22px}
  .package-btn{position:absolute;left:430px;top:327px;width:126px;height:44px;line-height:44px;font-size:18px;background:#5ab4e6}
  .package-device{position:absolute;left:740px;top:142px;width:345px;height:335px;border-radius:50% / 22%;background:linear-gradient(180deg,#3a4050,#1a1e28 60%,#101318)}

  /* feedback */
  .feedback{position:absolute;left:0;top:2125px;width:1200px;height:787px;text-align:center}
  .feedback-title{position:absolute;left:0;top:177px;width:1200px;font-size:26px;font-weight:700}
  .feedback-text{position:absolute;left:0;top:232px;width:1200px;font-size:20px;line-height:25px}
  .social-intro{position:absolute;left:0;top:452px;width:1200px;font-size:20px;line-height:26px}
  .social-links{position:absolute;left:0;top:530px;width:1200px;display:flex;justify-content:center;gap:40px}
  .social-link{display:flex;align-items:center;gap:10px;font-size:22px;color:var(--teal)}
  .social-link i{width:26px;height:26px;border:3px solid var(--teal);border-radius:6px}

  .site-footer{position:absolute;left:0;top:2912px;width:1200px;height:39px;background:var(--footer);color:var(--white);font-size:17px;line-height:39px;text-align:center}
</style>
</head>
<body>

<header class="site-header">
  <div class="brand"><span class="brand-dot"></span><span class="brand-name">Harbor Quill</span></div>
  <nav class="main-nav">
    <span class="current">about HQ</span><span>features</span><span>packages</span><span>contact us</span>
  </nav>
</header>

<section class="hero" role="img" aria-label="Evening city skyline behind a hand using a glowing smart tablet">
  <div class="hero-device" role="img" aria-label="Round smart speaker"></div>
  <h1 class="hero-title">SMARTER<br>INTERACTION</h1>
  <p class="hero-tagline">Get your hands on with smart technology</p>
  <a class="btn hero-btn">Find out more</a>
</section>

<section class="about">
  <h2 class="about-label">ABOUT HQ</h2>
  <h3 class="about-title">HARBOR QUILL HQ (OUR MISSION)</h3>
  <p class="about-text">Lorem ipsum dolor sit amet, consectetur adipiscing elit. In feugiat ligula ultricies dui pellentesque, dictum eleifend orci eleifend. Duis ut bibendum ipsum.Pellentesque eget justo sodales, tempus mauris non, venenatis odio. Nam rhoncus libero ligula. In hac habitasse platea dictumst.</p>
  <div class="about-art" role="img" aria-label="Line illustration of a flag on a mountain peak"></div>
  <div class="slider-dots"><span></span><span class="on"></span></div>
</section>

<section class="services">
  <div class="service-icon" role="img" aria-label="Theatre curtains icon"></div>
  <h3 class="service-title">Home Theatre Design</h3>
  <p class="service-text">Lorem ipsum dolor sit amet, consectetur adipiscing elit.<br>In feugiat ligula ultricies dui pellentesque, dictum eleifend orci eleifend.</p>
  <div class="service-photo" role="img" aria-label="Dark home cinema room with large screen and reclining seats"></div>
  <svg class="service-steps" viewBox="0 0 1200 643" aria-hidden="true">
    <defs>
      <linearGradient id="stepLine" x1="0" x2="1">
        <stop offset="0" stop-color="#52c7d8" stop-opacity="0"/>
        <stop offset="1" stop-color="#52c7d8"/>
      </linearGradient>
      <linearGradient id="stepRing" x1="0" y1="0" x2="1" y2="1">
        <stop offset="0" stop-color="#52c7d8"/>
        <stop offset="1" stop-color="#6a8ee6"/>
      </linearGradient>
    </defs>
    <line x1="140" y1="493" x2="462" y2="493" stroke="url(#stepLine)" stroke-width="6"/>
    <line x1="633" y1="493" x2="666" y2="493" stroke="#52c7d8" stroke-width="6"/>
    <line x1="838" y1="493" x2="874" y2="493" stroke="#52c7d8" stroke-width="6"/>
    <circle cx="547" cy="493" r="85" fill="none" stroke="url(#stepRing)" stroke-width="6"/>
    <circle cx="752" cy="493" r="85" fill="none" stroke="url(#stepRing)" stroke-width="6"/>
    <circle cx="960" cy="493" r="85" fill="none" stroke="url(#stepRing)" stroke-width="6"/>
    <g fill="none" stroke="url(#stepRing)" stroke-width="5">
      <circle cx="184" cy="583" r="26"/>
      <rect x="252" y="558" width="64" height="40" rx="2"/>
      <line x1="284" y1="598" x2="284" y2="608"/><line x1="268" y1="610" x2="300" y2="610"/>
      <rect x="366" y="556" width="24" height="34" rx="10"/>
      <line x1="378" y1="590" x2="378" y2="608"/><line x1="364" y1="610" x2="392" y2="610"/>
    </g>
    <text x="184" y="592" text-anchor="middle" font-family="Arimo, sans-serif" font-size="26" fill="#52c7d8">A</text>
  </svg>
  <span class="step-label" style="left:472px;top:465px">Design &amp;<br>Planning</span>
  <span class="step-label" style="left:677px;top:465px">Lightning &amp;<br>Technology</span>
  <span class="step-label" style="left:885px;top:479px">Seating</span>
</section>

<section class="package">
  <div class="package-ring">PLATINUM<br>PACKAGE</div>
  <span class="package-toggle" style="left:200px;background:#e6e6e6"></span>
  <span class="package-toggle" style="left:275px;background:var(--yellow)"></span>
  <p class="package-cost">PACKAGE COST: <b>$5000</b></p>
  <p class="package-text">Have all the bells and whistles of Silver and Gold, but adds a fully automated audio experience throughout the home</p>
  <a class="btn package-btn">Contact us</a>
  <div class="package-device" role="img" aria-label="Small round smart speaker with glowing blue ring"></div>
</section>

<section class="feedback">
  <h2 class="feedback-title">Your feedback has been sent successfully!</h2>
  <p class="feedback-text">Thank you for your feedback<br>We will get back to you in 24hrs</p>
  <p class="social-intro">In the meanwhile...<br>find us on</p>
  <div class="social-links">
    <span class="social-link"><i></i>chatterbay</span>
    <span class="social-link"><i></i>snapmeadow</span>
  </div>
</section>

<footer class="site-footer">© Harbor Quill. All rights reserved. Privacy Policy</footer>

</body>
</html>
```